Audio-Visual & Video Communications Business Requires a Cutting-edge Business Card Design

LinkVessel is a new Audio-Visual & Video Communications company in Cape Town, South Africa that is looking for a cutting-edge business card design. We sell these products to the Corporate, Education & Hospitality markets and will also host an Online Shop for companies and individuals to purchase our products online.

We are already using the following two colours in our logo and draft website. Please incorporate these colours into the design. Please note that our website is still in the design stage if you need to visit it. Green #a0ce4e & Dark Grey #333333.
Updates

Hi,

Please note that I have uploaded our logo in an .eps format.

Target Market(s)

Corporate Companies, Education Institutions & Hospitality Markets

Industry/Entity Type

Business

Requirements
Nice to have
• It would be great if you could incorporate the services that we offer.

1. Consultation & Design
2. Project Management
3. Supply & Installation
4. Onsite Support Personal
5. Online Shop

```html
<!DOCTYPE html>
<html lang="en">
<head>
<meta charset="utf-8">
<title>LinkVessel Business Cards</title>
<link rel="stylesheet" href="https://fonts.googleapis.com/css2?family=Ubuntu:wght@400;500;700&family=Open+Sans:wght@400;600&display=swap">
<style>
  :root {
    --green: #a0ce4e;
    --dark-grey: #333333;
    --mid-grey: #5a5a5a;
    --soft-grey: #6b6b6b;
    --paper: #f4f4f4;
    --card-dark: #1f1f1f;
    --stage: #2a2a2a;
  }
  * { box-sizing: border-box; margin: 0; padding: 0; }
  html, body {
    width: 1200px; height: 900px; overflow: hidden;
    background: var(--stage);
  }
  .canvas {
    position: relative; width: 1200px; height: 900px;
    display: flex; flex-direction: column; align-items: center;
    justify-content: center; gap: 24px;
  }
  .card {
    position: relative; width: 680px; height: 388px; overflow: hidden;
    box-shadow: 0 10px 30px rgba(0,0,0,.45);
  }

  /* Front card */
  .card--front { background: var(--paper); }
  .front__band {
    position: absolute; left: 0; right: 0; top: 176px; bottom: 0;
    background: var(--green);
    border-top: 10px solid var(--mid-grey);
  }
  .brand {
    position: absolute; display: flex; align-items: center; gap: 14px;
  }
  .brand__dot { border-radius: 50%; flex: none; }
  .brand__name {
    font-family: "Ubuntu", sans-serif; font-weight: 700; line-height: 1;
  }
  .card--front .brand { left: 48px; top: 96px; }
  .card--front .brand__dot { width: 44px; height: 44px; background: var(--green); }
  .card--front .brand__name { font-size: 52px; color: var(--dark-grey); }

  .person {
    position: absolute; left: 48px; top: 222px; color: var(--dark-grey);
  }
  .person__name {
    font-family: "Ubuntu", sans-serif; font-weight: 700; font-size: 26px;
  }
  .person__title {
    font-family: "Open Sans", sans-serif; font-size: 13px; margin-top: 2px;
  }
  .person__address {
    font-family: "Open Sans", sans-serif; font-size: 14px; line-height: 1.35;
    margin-top: 18px;
  }
  .contacts {
    position: absolute; left: 400px; top: 218px; list-style: none;
    font-family: "Open Sans", sans-serif; font-size: 14px; color: var(--dark-grey);
  }
  .contacts li { display: flex; align-items: center; gap: 10px; height: 24px; }
  .contacts svg { width: 14px; height: 14px; flex: none; }

  /* Back card */
  .card--back { background: var(--card-dark); text-align: center; }
  .card--back .brand {
    left: 0; right: 0; top: 150px; justify-content: center;
  }
  .card--back .brand__dot { width: 40px; height: 40px; background: var(--green); }
  .card--back .brand__name { font-size: 50px; color: var(--green); }
  .services {
    position: absolute; left: 0; right: 0; top: 252px;
    font-family: "Open Sans", sans-serif; font-size: 16px; line-height: 1.5;
    color: var(--green);
  }
  .services__muted { color: var(--soft-grey); }
  .services__sep { color: var(--green); margin: 0 6px; }
</style>
</head>
<body>
<main class="canvas">

  <section class="card card--front" aria-label="Business card front">
    <div class="front__band"></div>
    <div class="brand">
      <span class="brand__dot"></span>
      <span class="brand__name">LinkVessel</span>
    </div>
    <div class="person">
      <p class="person__name">Marla Quinn</p>
      <p class="person__title">Managing Director</p>
      <p class="person__address">Address 14 Harbour Lane<br>Greenpoint 8005 CAPE TOWN</p>
    </div>
    <ul class="contacts">
      <li>
        <svg viewBox="0 0 16 16" aria-hidden="true"><path fill="#333333" d="M3 1h3l1 4-2 1a9 9 0 0 0 5 5l1-2 4 1v3c0 1-1 2-2 2A13 13 0 0 1 1 3c0-1 1-2 2-2z"/></svg>
        <span>+0 555 010 200</span>
      </li>
      <li>
        <svg viewBox="0 0 16 16" aria-hidden="true"><rect x="4" y="1" width="8" height="5" fill="#333333"/><rect x="1" y="6" width="14" height="6" rx="1" fill="#333333"/><rect x="4" y="10" width="8" height="5" fill="#f4f4f4" stroke="#333333"/></svg>
        <span>+0 555 010 200</span>
      </li>
      <li>
        <svg viewBox="0 0 16 16" aria-hidden="true"><rect x="1" y="3" width="14" height="10" rx="1" fill="#333333"/><path d="M1 4l7 5 7-5" fill="none" stroke="#a0ce4e" stroke-width="1.4"/></svg>
        <span>info@LinkVessel.com</span>
      </li>
      <li>
        <svg viewBox="0 0 16 16" aria-hidden="true"><circle cx="8" cy="8" r="6.5" fill="none" stroke="#333333" stroke-width="1.5"/><ellipse cx="8" cy="8" rx="2.6" ry="6.5" fill="none" stroke="#333333" stroke-width="1.2"/><path d="M1.5 8h13" stroke="#333333" stroke-width="1.2"/></svg>
        <span>www.LinkVessel.com</span>
      </li>
    </ul>
  </section>

  <section class="card card--back" aria-label="Business card back">
    <div class="brand">
      <span class="brand__dot"></span>
      <span class="brand__name">LinkVessel</span>
    </div>
    <p class="services">
      Consultation &amp; Design<span class="services__sep">|</span><span class="services__muted">Project Management</span><span class="services__sep">|</span>Supply &amp; Installation<br>
      Onsite Support Personal<span class="services__sep">|</span>Online Shop
    </p>
  </section>

</main>
</body>
</html>
```